Small rum distillery looking for bottle design

Small rum distillery in Estonia. Looking for bottle lable design. It should be simple but at the same time point out from the variety of other bottles.
As we are a small nordic country, design can be some how nordic or represent our country. It can also have some connection with sailing or sea as we know it pirates love it.
Bottle we are using is Corvane 540

Industry/Entity Type

food and beverage

Other font styles liked:
• Baskerville

```html
<!DOCTYPE html>
<html lang="en">
<head>
<meta charset="utf-8">
<title>Harvel Distillery Rum Label</title>
<link href="https://fonts.googleapis.com/css2?family=Libre+Baskerville:wght@400;700&family=Roboto+Slab:wght@800&family=Open+Sans:wght@400;600&display=swap" rel="stylesheet">
<style>
  :root {
    --backdrop: #0c0c0d;
    --paper: #f3f0eb;
    --rum-red: #a8302c;
    --deep-red: #7d1f1c;
    --ink: #3a3a3a;
    --soft-ink: #6b6b6b;
    --ornament-grey: #9a9a9a;
  }
  * { margin: 0; padding: 0; box-sizing: border-box; }
  html, body { width: 1200px; height: 1200px; overflow: hidden; }
  body { background: var(--backdrop); position: relative; font-family: "Open Sans", sans-serif; }

  .label { position: absolute; inset: 0; }
  .label-frame { position: absolute; left: 0; top: 0; }

  .brand-seal {
    position: absolute; left: 505px; top: 180px; width: 190px; height: 150px;
    display: flex; flex-direction: column; align-items: center; justify-content: center; gap: 10px;
  }
  .brand-dot { width: 34px; height: 34px; border-radius: 50%; background: var(--rum-red); }
  .brand-name {
    font-family: "Libre Baskerville", serif; font-weight: 400; color: var(--soft-ink);
    font-size: 19px; letter-spacing: 2px; text-align: center; line-height: 1.35; text-transform: uppercase;
  }

  .text-column {
    position: absolute; left: 290px; top: 530px; width: 310px;
  }
  .product-title {
    font-family: "Roboto Slab", serif; font-weight: 800; font-size: 112px; line-height: 1;
    color: var(--rum-red); letter-spacing: 1px; white-space: nowrap;
  }
  .product-tagline {
    margin-top: 14px;
    font-family: "Open Sans", sans-serif; font-weight: 600; font-size: 14.5px; color: var(--soft-ink);
    text-transform: uppercase; letter-spacing: 0; white-space: nowrap;
  }

  .spec-row { display: flex; gap: 34px; margin-top: 26px; padding-left: 8px; }
  .spec-badge {
    width: 112px; height: 112px; border-radius: 50%;
    border: 3px solid var(--ornament-grey); outline: 2px solid var(--ornament-grey); outline-offset: 5px;
    display: flex; flex-direction: column; align-items: center; justify-content: center;
    background: var(--paper);
  }
  .spec-label { font-size: 14px; color: var(--ink); text-transform: uppercase; }
  .spec-value { font-size: 28px; color: var(--ink); line-height: 1.1; }
  .spec-badge--batch .spec-value { color: var(--rum-red); }

  .established { margin-top: 30px; font-size: 26px; color: var(--ink); }
  .established-year { color: var(--rum-red); }
</style>
</head>
<body>
  <main class="label">
    <svg class="label-frame" width="1200" height="1200" viewBox="0 0 1200 1200">
      <defs>
        <radialGradient id="wreathTone" cx="50%" cy="50%" r="50%">
          <stop offset="70%" stop-color="#c9c6c2"/>
          <stop offset="100%" stop-color="#8e8a86"/>
        </radialGradient>
        <linearGradient id="shipTone" x1="0" y1="0" x2="0" y2="1">
          <stop offset="0%" stop-color="#e2dfda"/>
          <stop offset="100%" stop-color="#8f8b86"/>
        </linearGradient>
      </defs>
      <g class="banner-ribbons" role="img" aria-label="Red ribbon banners unfurling on either side of the crest">
        <path d="M230 250 L420 215 L420 330 L260 355 L290 300 Z" fill="var(--rum-red)"/>
        <path d="M970 250 L780 215 L780 330 L940 355 L910 300 Z" fill="var(--rum-red)"/>
      </g>
      <path class="panel-outer" d="M280 400 H920 A30 30 0 0 0 950 430 V1030 A30 30 0 0 0 920 1060 H280 A30 30 0 0 0 250 1030 V430 A30 30 0 0 0 280 400 Z"
            fill="var(--paper)" stroke="var(--rum-red)" stroke-width="9"/>
      <path class="panel-inner" d="M292 414 H908 A24 24 0 0 0 936 442 V1018 A24 24 0 0 0 908 1046 H292 A24 24 0 0 0 264 1018 V442 A24 24 0 0 0 292 414 Z"
            fill="none" stroke="var(--rum-red)" stroke-width="2"/>
      <circle class="crest-wreath" cx="600" cy="255" r="150" fill="url(#wreathTone)"
              role="img" aria-label="Crowned rope and leaf wreath around the distillery seal"/>
      <circle class="crest-ring" cx="600" cy="255" r="112" fill="none" stroke="var(--rum-red)" stroke-width="8"/>
      <circle class="crest-center" cx="600" cy="255" r="102" fill="var(--paper)"/>
      <rect class="ship-art" x="630" y="520" width="296" height="516" rx="6" fill="url(#shipTone)"
            role="img" aria-label="Engraved sailing galleon with anchor on the sea"/>
    </svg>

    <div class="brand-seal">
      <span class="brand-dot"></span>
      <p class="brand-name">Harvel<br>Distillery</p>
    </div>

    <div class="text-column">
      <h1 class="product-title">RUM</h1>
      <p class="product-tagline">Small rum distillery in Estonia</p>
      <div class="spec-row">
        <div class="spec-badge spec-badge--abv">
          <span class="spec-label">Alc/Vol</span>
          <span class="spec-value">46%</span>
        </div>
        <div class="spec-badge spec-badge--batch">
          <span class="spec-label">Batch No</span>
          <span class="spec-value">002</span>
        </div>
      </div>
      <p class="established">EST'D <span class="established-year">2015</span></p>
    </div>
  </main>
</body>
</html>
```